Professional DJ Business Card

Business card for giving out to clubs and venues or interested groups that are in need of a professional DJ. I want something artistic and catchy/alluring, with a minimalist approach that gets just the vital amount of info and leaves the rest for inquiry via contacting me. Ideally I would like one side to have an image of something cool like an eye and my name, then the other side be the contact info, I am definitely feeling a black or dark colored card, but I am open to other designs. I am uploading a picture that I made that reflects a little of what I am *kind of* looking for.

Industry/Entity Type

Business

Contact Information for Business Card

Tomas Halvik (Voxtel)
Professional DJ (West Coast)
EDM (Deep/House/Techno), Hip Hop, Latin, Trap.
Cell: 555-274-9163
Email: Voxtelofficial@mailnest.net
www.beatcloudia.net/yourtuneisfading

```html
<!DOCTYPE html>
<html lang="en">
<head>
<meta charset="UTF-8">
<title>Voxtel – DJ Business Card</title>
<link href="https://fonts.googleapis.com/css2?family=Open+Sans:wght@400;600&display=swap" rel="stylesheet">
<style>
  :root {
    --page-bg: #9a9a9a;
    --card-dark: #0a0d0b;
    --card-light: #d5d6dd;
    --ink-light: #e6e6e6;
    --ink-dark: #111111;
    --ink-muted: #2a2a2a;
    --sketch-tone: #8d8f8e;
  }
  * { margin: 0; padding: 0; box-sizing: border-box; }
  html, body {
    width: 1105px; height: 1200px; overflow: hidden;
    background: var(--page-bg);
    font-family: "Open Sans", Arial, sans-serif;
  }
  .canvas { position: relative; width: 1105px; height: 1200px; }
  .card {
    position: absolute; left: 184px; width: 744px; height: 425px;
    background: var(--card-dark); overflow: hidden;
  }
  .card--front { top: 119px; }
  .card--back { top: 638px; }
  .front-curve { position: absolute; inset: 0; }
  .identity {
    position: absolute; right: 42px; top: 22px; text-align: right; color: var(--ink-dark);
  }
  .identity__name { font-size: 25px; font-weight: 600; line-height: 1.25; }
  .identity__role { font-size: 18.5px; font-weight: 400; color: var(--ink-muted); line-height: 1.3; }
  .wordmark {
    position: absolute; color: var(--ink-light); font-weight: 600; letter-spacing: 1px;
  }
  .wordmark--front { left: 44px; top: 168px; font-size: 60px; line-height: 1; }
  .wordmark--back { left: 170px; top: 214px; font-size: 76px; line-height: 1; }
  .contact-list {
    position: absolute; left: 44px; top: 306px; list-style: none; color: var(--ink-light);
    font-size: 19.5px;
  }
  .contact-list li { display: flex; align-items: center; height: 29px; }
  .contact-list svg { width: 20px; height: 20px; margin-right: 15px; flex: none; }
  .genres {
    position: absolute; right: 38px; top: 331px; text-align: right; color: var(--ink-light);
    font-size: 19.5px; line-height: 27px;
  }
  .eye-sketch {
    position: absolute; left: 245px; top: 112px; width: 345px; height: 120px;
    background: radial-gradient(ellipse at 45% 55%, rgba(141,143,142,0.55) 0%, rgba(141,143,142,0.18) 45%, rgba(10,13,11,0) 75%);
  }
</style>
</head>
<body>
<main class="canvas">
  <section class="card card--front">
    <svg class="front-curve" width="744" height="425" viewBox="0 0 744 425" aria-hidden="true">
      <rect width="744" height="425" fill="var(--card-light)"/>
      <path d="M0,43 Q372,36 744,320 L744,425 L0,425 Z" fill="var(--card-dark)"/>
    </svg>
    <div class="identity">
      <p class="identity__name">Tomas Halvik (Voxtel)</p>
      <p class="identity__role">Professional DJ (West Coast)</p>
    </div>
    <p class="wordmark wordmark--front">Voxtel</p>
    <ul class="contact-list">
      <li>
        <svg viewBox="0 0 20 20" aria-hidden="true"><rect x="5" y="1" width="10" height="18" rx="2" fill="none" stroke="var(--ink-light)" stroke-width="1.8"/><line x1="8" y1="16" x2="12" y2="16" stroke="var(--ink-light)" stroke-width="1.5"/></svg>
        555-274-9163
      </li>
      <li>
        <svg viewBox="0 0 20 20" aria-hidden="true"><rect x="2" y="5" width="16" height="11" fill="var(--ink-light)"/><path d="M2,5 L10,11 L18,5" fill="none" stroke="var(--card-dark)" stroke-width="1.4"/></svg>
        Voxtelofficial@mailnest.net
      </li>
      <li>
        <svg viewBox="0 0 20 20" aria-hidden="true"><circle cx="10" cy="10" r="6" fill="var(--ink-light)"/></svg>
        yourtuneisfading
      </li>
    </ul>
    <p class="genres">EDM (Deep/House/Techno)<br>Hip Hop, Latin, Trap</p>
  </section>

  <section class="card card--back">
    <div class="eye-sketch" role="img" aria-label="Sketched eye with radiating lines"></div>
    <p class="wordmark wordmark--back">Voxtel</p>
  </section>
</main>
</body>
</html>
```